Pediatric Practice Flyer Design

I need marketing flyer created for distribution. It is for a pediatric clinic. Need some realistic eye catching design and content. I already have a logo that will go on top of the flyer. I will be using quellomark for flyer print service. So need it copyable for printing. Again, need eye catching content as well. We are planning on opening the clinic in December.

```html
<!DOCTYPE html>
<html lang="en">
<head>
<meta charset="utf-8">
<title>Maplebud Kids Care Pediatrics – Flyer</title>
<link rel="stylesheet" href="https://fonts.googleapis.com/css2?family=Poppins:wght@400;500;600;700;800&display=swap">
<style>
  :root{
    --red:#e42230; --yellow:#ffd21f; --purple:#6a2c91; --orange:#f7941d;
    --teal:#12907f; --blue:#1a73c0; --ink:#1d1d1b; --paper:#ffffff; --bg:#e9e9ea;
  }
  *{box-sizing:border-box;margin:0;padding:0}
  html,body{width:1200px;height:2931px;overflow:hidden;background:var(--bg);font-family:'Poppins',sans-serif;color:var(--ink)}
  .flyer{position:absolute;left:50px;top:752px;width:1100px;height:1426px;background:var(--paper);overflow:hidden;box-shadow:0 10px 40px rgba(0,0,0,.25)}
  .abs{position:absolute}
  .brand{left:44px;top:58px;display:flex;align-items:center;gap:14px}
  .brand-dot{width:62px;height:62px;border-radius:50%;background:var(--red)}
  .brand-name{font-weight:700;font-size:40px;color:var(--red);line-height:1.05}
  .hero-band{left:0;top:180px;width:1100px;height:203px;background:var(--red)}
  .hero-title{left:44px;top:193px;font-weight:800;font-size:52px;line-height:1.0;color:#fff;text-transform:uppercase}
  .hero-title .hl{color:var(--yellow)}
  .offer{left:0;top:383px;width:600px;height:67px;background:var(--purple);clip-path:polygon(0 0,100% 0,94% 100%,0 100%)}
  .offer-text{left:120px;top:386px;font-weight:700;font-size:38px;color:#fff;line-height:60px}
  .offer-text .hl{color:var(--yellow)}
  .offer-text sup{font-size:20px}
  .offer-icon{left:50px;top:393px}
  .hero-art{left:0;top:0}
  .about-title{left:44px;top:462px;font-weight:800;font-size:32px}
  .about-title span{color:var(--purple)}
  .about-text{left:44px;top:510px;width:1010px;font-size:13.5px;line-height:1.3}
  .about-text b{color:var(--purple);font-weight:600}
  .services-box{left:44px;top:590px;width:1010px;height:200px;border:2px solid var(--teal);border-radius:14px}
  .services-pill{left:345px;top:565px;width:410px;height:56px;background:var(--teal);border-radius:14px;color:#fff;font-weight:600;font-size:31px;text-align:center;line-height:56px}
  .service{position:absolute;top:640px;width:260px;text-align:center}
  .service .ring{width:117px;height:117px;margin:0 auto;border-radius:50%;border:3px solid var(--orange);background:#fff;display:flex;align-items:center;justify-content:center}
  .service .ring i{width:101px;height:101px;border-radius:50%;border:3px solid var(--purple);display:flex;align-items:center;justify-content:center}
  .service .label{display:inline-block;margin-top:10px;padding:0 10px;background:#fff;font-weight:500;font-size:22px;line-height:30px;white-space:nowrap;position:relative;z-index:2}
  .sep{position:absolute;top:650px;width:3px;height:110px;background:linear-gradient(#fff,#e6e6e6,#fff)}
  .provider-panel{left:43px;top:831px;width:1010px;height:346px;background:linear-gradient(90deg,#1565b3,#1a7cc8)}
  .provider-tab{left:194px;top:831px;width:350px;height:48px;background:var(--orange);clip-path:polygon(0 0,100% 0,92% 100%,0 100%);color:#fff;font-weight:500;font-size:26px;line-height:48px;padding-left:18px}
  .provider-photo{left:11px;top:813px;width:223px;height:364px;background:linear-gradient(180deg,#2a2a33,#3a4050 60%,#20252f);border-radius:110px 110px 0 0}
  .provider-bio{left:254px;top:916px;width:780px;color:#fff;font-size:12.5px;line-height:1.3}
  .provider-bio h3{font-size:18px;font-weight:600;line-height:1.1}
  .provider-bio p{margin-bottom:12px}
  .opening{left:43px;top:1212px;font-size:33px;line-height:1.25;color:var(--purple)}
  .opening b{color:var(--red);font-weight:700}
  .divider{left:587px;top:1200px;width:2px;height:100px;background:var(--orange)}
  .perks{left:633px;top:1203px;font-size:26px;color:var(--ink)}
  .perks li{list-style:none;display:flex;align-items:center;gap:22px;height:46px}
  .register{left:0;top:1337px;width:350px;height:89px;background:var(--red);clip-path:polygon(0 0,92% 0,100% 100%,0 100%);color:#fff;font-weight:700;font-size:28px;line-height:89px;padding-left:43px}
  .register span{color:var(--yellow)}
  .contact{top:1352px;font-size:15px;font-weight:500;line-height:27px}
  .contact li{list-style:none;display:flex;align-items:center;gap:10px;white-space:nowrap}
  .vrule{top:1350px;width:1px;height:60px;background:var(--orange)}
</style>
</head>
<body>
<main class="flyer">

  <div class="abs hero-band"></div>

  <svg class="abs hero-art" width="1100" height="520" viewBox="0 0 1100 520">
    <polygon points="839,20 567,459 1100,459 1100,190" fill="#fff"/>
    <polygon points="839,38 590,448 1100,448 1100,200" fill="#c9a88f" role="img" aria-label="Photo of a mother playing on the floor with her young daughter"/>
    <polyline points="1100,198 839,20 567,459 1100,459" fill="none" stroke="#e42230" stroke-width="8"/>
    <polyline points="673,492 1100,492" fill="none" stroke="#f7941d" stroke-width="6"/>
    <polyline points="673,492 919,16 1100,370" fill="none" stroke="#f7941d" stroke-width="6"/>
  </svg>

  <div class="abs brand">
    <div class="brand-dot"></div>
    <div class="brand-name">Maplebud Kids<br>Care Pediatrics</div>
  </div>

  <h1 class="abs hero-title">Welcome to<br><span class="hl">Maplebud Kids Care</span><br>Pediatric!</h1>

  <div class="abs offer"></div>
  <svg class="abs offer-icon" width="46" height="46" viewBox="0 0 46 46" fill="#fff">
    <circle cx="20" cy="10" r="6"/><rect x="10" y="18" width="20" height="14" rx="4"/>
    <rect x="4" y="34" width="36" height="4"/><rect x="30" y="4" width="12" height="8" rx="2"/>
  </svg>
  <div class="abs offer-text"><span class="hl">FREE</span> 1<sup>st</sup> consultation</div>

  <h2 class="abs about-title">ABOUT <span>US</span></h2>
  <p class="abs about-text">Where we believe it takes a community to raise a child. We are excited to be small yet important member of the community to help raise a healthy and happy child. Our goal is to provide personalized and comprehensive care collectively that consists of the Parent,<br><b>Child, Provider Triangle.</b></p>

  <div class="abs services-box"></div>
  <div class="abs services-pill">SERVICES WE PROVIDE</div>

  <div class="service" style="left:58px">
    <div class="ring"><i><svg width="50" height="50" viewBox="0 0 50 50" fill="#6a2c91"><path d="M25 26 L14 15 a6 6 0 0 1 11-6 a6 6 0 0 1 11 6z"/><path d="M4 34 h10 l10 4 h12 l10-8 v6 l-12 10 h-18 l-12-4z"/></svg></i></div>
    <span class="label">Well Care</span>
  </div>
  <div class="sep" style="left:330px"></div>
  <div class="service" style="left:264px">
    <div class="ring"><i><svg width="50" height="50" viewBox="0 0 50 50" fill="#6a2c91"><rect x="6" y="6" width="6" height="24" rx="3"/><circle cx="9" cy="34" r="6"/><circle cx="32" cy="18" r="10"/><path d="M16 46 a16 14 0 0 1 32 0z"/></svg></i></div>
    <span class="label">Sick Care</span>
  </div>
  <div class="sep" style="left:500px"></div>
  <div class="service" style="left:490px">
    <div class="ring"><i><svg width="50" height="50" viewBox="0 0 50 50" fill="none" stroke="#6a2c91" stroke-width="3"><rect x="8" y="8" width="28" height="36" rx="3"/><rect x="16" y="4" width="12" height="7" rx="2" fill="#6a2c91"/><path d="M14 20h16M14 27h16M14 34h10"/><circle cx="38" cy="38" r="7" fill="#fff"/><path d="M35 38l2 2 4-4"/></svg></i></div>
    <span class="label">Impact testing</span>
  </div>
  <div class="sep" style="left:712px"></div>
  <div class="service" style="left:740px">
    <div class="ring"><i><svg width="50" height="50" viewBox="0 0 50 50" fill="none" stroke="#6a2c91" stroke-width="3"><rect x="8" y="6" width="28" height="38" rx="3"/><path d="M14 22h4M14 30h4M22 22h8M22 30h8"/><path d="M22 12l2 4 4 .5-3 3 .8 4-3.8-2-3.8 2 .8-4-3-3 4-.5z" fill="#6a2c91" stroke="none"/><path d="M34 34l8 8" stroke-width="4"/></svg></i></div>
    <span class="label">Additional services</span>
  </div>

  <div class="abs provider-panel"></div>
  <div class="abs provider-photo" role="img" aria-label="Portrait photo of the pediatrician in a dark blazer"></div>
  <div class="abs provider-tab">Meet Our Providor</div>
  <div class="abs provider-bio">
    <h3>Dr. Lena Haddad</h3>
    <p>is an experienced and qualified Pediatrician, previously served the communities of Fairmont and Westbury, VA for several years.</p>
    <p>Where she was recognized in the Capital Region Top Doctors 2019 magazine as well as Top Female Doctor in the city of Fairmont, Virginia. For past few years she had been serving the underserved population of Oak Hollow, NC.</p>
    <p>She obtained her medical degree from the Crescent Valley Medical College. After numerous research and observership positions in North Carolina including the Cedar Clinic, Community Care Alliance and Piedmont State University, and abroad including Riverside Children's Hospital and Northgate Hospital, she decided to pursue her passion of working with children and trained in Pediatrics at Southwest University Health Sciences Center in Mesa Ridge, Texas.</p>
  </div>

  <p class="abs opening">We are planning on <b>OPENING</b><br><b>THE CLINIC</b> in December</p>
  <div class="abs divider"></div>
  <ul class="abs perks">
    <li><svg width="30" height="32" viewBox="0 0 30 32" fill="#6a2c91"><circle cx="13" cy="8" r="7"/><path d="M0 32 a13 12 0 0 1 26 0z"/><circle cx="24" cy="22" r="6" fill="#1a73c0"/></svg>Accepting new patients</li>
    <li><svg width="30" height="32" viewBox="0 0 30 32" fill="#6a2c91"><circle cx="15" cy="9" r="8"/><path d="M1 32 a14 12 0 0 1 28 0z"/><circle cx="24" cy="24" r="4" fill="#1a73c0"/></svg>Pediatrician</li>
  </ul>

  <div class="abs register">REGISTER <span>TODAY</span></div>
  <ul class="abs contact" style="left:367px">
    <li><svg width="16" height="16" viewBox="0 0 16 16" fill="#1a73c0"><path d="M3 1l3 3-2 2a9 9 0 0 0 6 6l2-2 3 3-2 2C6 15 1 10 1 3z"/></svg>919-555-0184</li>
    <li><svg width="16" height="16" viewBox="0 0 16 16" fill="#1a73c0"><rect x="1" y="5" width="14" height="10" rx="1"/><rect x="4" y="1" width="8" height="5"/></svg>919-555-0127</li>
  </ul>
  <div class="abs vrule" style="left:545px"></div>
  <ul class="abs contact" style="left:566px">
    <li style="align-items:flex-start"><svg width="16" height="20" viewBox="0 0 16 20" fill="#1a73c0" style="margin-top:4px"><path d="M8 0a7 7 0 0 1 7 7c0 5-7 12-7 12S1 12 1 7a7 7 0 0 1 7-7z"/><circle cx="8" cy="7" r="3" fill="#fff"/></svg><span style="line-height:20px">48 Linden Row, Suite<br>12, Brookfield NC 27000</span></li>
  </ul>
  <div class="abs vrule" style="left:780px"></div>
  <ul class="abs contact" style="left:802px">
    <li><svg width="16" height="14" viewBox="0 0 16 14" fill="#1a73c0"><rect x="0" y="1" width="16" height="12" rx="1"/><path d="M1 2l7 6 7-6" stroke="#fff" fill="none" stroke-width="1.5"/></svg>office@maplebudkids.com</li>
    <li><svg width="16" height="16" viewBox="0 0 16 16" fill="none" stroke="#1a73c0" stroke-width="1.6"><circle cx="8" cy="8" r="7"/><ellipse cx="8" cy="8" rx="3" ry="7"/><path d="M1 8h14"/></svg>www.maplebudkids.com</li>
  </ul>

</main>
</body>
</html>
```